Torvin Electrics Flyer Design Advertising

I am after an A5 Flyer design to help promote my electrical services business.
I would like to have information on what my business offers, photos of electrical work, and specials/deals for an amount of time.

Industry/Entity Type

Electrician

Font styles to use
Sans Serif

Colors
0292cd
33a6d7
85cae6
3176b5
333333
1b1b1b
ffffff
5c5c5c
474747

Requirements
Must have
• Specialising in New homes, renovations and commercial projects
• Contact details:
• ph. 0457 613 948
• email admin@torvinelectrics.com.au
• facebook TorvinElectrics
• Specials/Deals:
• 10% off all electrical services
• or
• Free LED downlights on installation
• *Terms conditions apply
• ALL RESIDENTIAL & COMMERCIAL ELECTRICAL SERVICES
• - New Home installations
• - Commercial projects
• - Shop fit outs
• - Renovations
• - Smoke Detectors
• - Air Conditioning and Ceiling Fans
• - Garden Lighting
• - Oven and Cooktop Installations
• - Power Point installation
• - LED lighting upgrades
• - Security Lighting
• - Switchboard upgrades
• - Test and Tag
• - Commercial Property
• - General Electrical Maintenance

```html
<!DOCTYPE html>
<html lang="en">
<head>
<meta charset="utf-8">
<title>Torvin Electrics Flyer</title>
<link href="https://fonts.googleapis.com/css2?family=Orbitron:wght@700;800;900&family=Oswald:wght@500;600&family=Roboto:wght@400;500;700&display=swap" rel="stylesheet">
<style>
  :root{
    --blue:#0292cd;
    --blue-mid:#33a6d7;
    --blue-light:#85cae6;
    --blue-deep:#3176b5;
    --ink:#333333;
    --ink-dark:#1b1b1b;
    --white:#ffffff;
    --grey:#5c5c5c;
    --grey-dark:#474747;
    --red:#e8203a;
    --canvas:#d9d9d9;
  }
  *{margin:0;padding:0;box-sizing:border-box}
  html,body{width:1200px;height:1200px;overflow:hidden;background:var(--canvas)}
  .flyer{position:absolute;left:245px;top:103px;width:710px;height:994px;background:var(--white);overflow:hidden;font-family:"Roboto",sans-serif;color:var(--ink)}
  .artwork{position:absolute;left:0;top:0;width:710px;height:994px}

  .brand{position:absolute;left:39px;top:27px;display:flex;align-items:center;gap:12px}
  .brand-dot{width:88px;height:88px;border-radius:50%;background:var(--blue)}
  .brand-name{font-family:"Roboto",sans-serif;font-weight:700;font-size:24px;color:var(--white);letter-spacing:1px;white-space:nowrap}

  .offer-badge{position:absolute;left:514px;top:0;width:151px;height:230px;color:var(--white);font-family:"Oswald",sans-serif;font-weight:600;line-height:1;text-align:center}
  .offer-badge > div{position:absolute;left:0;width:151px;white-space:nowrap}
  .offer-big{top:36px;font-size:52px;letter-spacing:-1px}
  .offer-big sup{font-size:24px;vertical-align:22px}
  .offer-line{font-size:12px;font-weight:500;letter-spacing:-.3px}
  .offer-line.l1{top:89px}
  .offer-line.l2{top:180px;font-size:11.5px}
  .offer-or{top:117px;font-size:12px;font-weight:500}
  .offer-free{top:134px;font-size:42px;letter-spacing:-1px}
  .offer-terms{top:201px;font-family:"Roboto",sans-serif;font-size:9px;font-weight:400}

  .headline{position:absolute;left:34px;top:0;font-family:"Orbitron",sans-serif;font-weight:900;line-height:1;white-space:nowrap}
  .headline > div{position:absolute;left:0}
  .h-a{top:398px;font-size:40px;color:var(--white)}
  .h-b{top:440px;font-size:54px;color:var(--white)}
  .h-c{top:493px;font-size:37px;color:var(--ink)}
  .h-d{top:531px;font-size:22px;color:var(--ink);font-weight:800}

  .services-title{position:absolute;left:34px;top:621px;font-family:"Orbitron",sans-serif;font-weight:800;font-size:16px;line-height:18px;color:var(--blue);white-space:nowrap}
  .service-list{position:absolute;top:675px;list-style:none;font-size:13px;line-height:14px;color:var(--grey-dark)}
  .service-list li{position:relative;padding-left:17px;margin-bottom:6px;white-space:nowrap}
  .service-list li::before{content:"";position:absolute;left:0;top:2px;width:9px;height:9px;border:1.3px solid var(--blue)}
  .service-list li::after{content:"";position:absolute;left:3px;top:1px;width:4px;height:8px;border-right:2px solid var(--blue);border-bottom:2px solid var(--blue);transform:rotate(40deg)}
  .list-left{left:34px}
  .list-right{left:245px}
  .list-divider{position:absolute;left:214px;top:672px;width:1px;height:178px;background:#e3e3e3}

  .contact-title{position:absolute;left:39px;top:877px;font-family:"Orbitron",sans-serif;font-weight:800;font-size:16px;color:var(--red);white-space:nowrap}
  .contact-list{position:absolute;left:34px;top:898px;list-style:none;color:var(--white);font-size:16px;line-height:22px}
  .contact-list li{display:flex;align-items:center;gap:10px;white-space:nowrap}
  .contact-icon{width:14px;height:14px;flex:none}
  .contact-dot{width:14px;height:14px;border-radius:50%;background:var(--white);flex:none}

  .offer-ends{position:absolute;left:291px;top:877px;font-family:"Orbitron",sans-serif;font-weight:800;font-size:16px;color:var(--blue);white-space:nowrap}
  .offer-date{position:absolute;left:313px;top:893px;font-size:26px;color:var(--ink)}
  .licence{position:absolute;left:336px;top:931px;font-size:12px;line-height:17px;color:var(--ink);white-space:nowrap}
  .licence b{color:var(--blue);font-weight:500}
  .licence .abn{padding-left:11px}
</style>
</head>
<body>
<div class="flyer">
  <svg class="artwork" viewBox="0 0 710 994" xmlns="http://www.w3.org/2000/svg">
    <defs>
      <linearGradient id="heroGrad" x1="0" y1="0" x2="0" y2="1">
        <stop offset="0" stop-color="#8a9bbf"/>
        <stop offset=".35" stop-color="#c7c3c8"/>
        <stop offset=".65" stop-color="#a7784a"/>
        <stop offset="1" stop-color="#4b3a26"/>
      </linearGradient>
      <linearGradient id="greyGrad" x1="0" y1="0" x2="1" y2="1">
        <stop offset="0" stop-color="#8d8d8d"/>
        <stop offset="1" stop-color="#e6e6e6"/>
      </linearGradient>
      <linearGradient id="warmGrad" x1="0" y1="0" x2="0" y2="1">
        <stop offset="0" stop-color="#3f5a6a"/>
        <stop offset="1" stop-color="#8a5a32"/>
      </linearGradient>
      <linearGradient id="poolGrad" x1="0" y1="0" x2="0" y2="1">
        <stop offset="0" stop-color="#6e6a72"/>
        <stop offset="1" stop-color="#1d7fc1"/>
      </linearGradient>
      <linearGradient id="gardenGrad" x1="0" y1="0" x2="0" y2="1">
        <stop offset="0" stop-color="#3b4a5a"/>
        <stop offset=".6" stop-color="#4f7b3a"/>
        <stop offset="1" stop-color="#1a5fb0"/>
      </linearGradient>
      <linearGradient id="whiteGrad" x1="0" y1="0" x2="1" y2="1">
        <stop offset="0" stop-color="#f2f2f2"/>
        <stop offset="1" stop-color="#6b6b6b"/>
      </linearGradient>
      <linearGradient id="deckGrad" x1="0" y1="0" x2="0" y2="1">
        <stop offset="0" stop-color="#5a5550"/>
        <stop offset="1" stop-color="#7a4b2a"/>
      </linearGradient>
    </defs>

    <g role="img" aria-label="Photo of a lit outdoor pergola and timber deck at dusk">
      <polygon points="0,0 710,0 710,245 584,371 0,371" fill="url(#heroGrad)"/>
    </g>

    <polygon points="0,375 579,375 367,582 0,582" fill="var(--blue)"/>

    <g role="img" aria-label="Photo of a modern white kitchen with pendant lights">
      <polygon points="710,252 497,463 710,700" fill="url(#greyGrad)"/>
    </g>
    <g role="img" aria-label="Photo of a lit courtyard lounge at night">
      <polygon points="479,491 577,592 479,694 373,592" fill="url(#warmGrad)"/>
    </g>
    <g role="img" aria-label="Photo of a house exterior beside a lit pool">
      <polygon points="587,606 683,714 587,810 479,706" fill="url(#poolGrad)"/>
    </g>
    <g role="img" aria-label="Photo of a garden wall and pool lit at night">
      <polygon points="475,726 583,826 475,930 383,826" fill="url(#gardenGrad)"/>
    </g>
    <g role="img" aria-label="Photo of a bright white interior with pendant lights">
      <polygon points="710,720 587,826 710,935" fill="url(#whiteGrad)"/>
    </g>
    <g role="img" aria-label="Photo of a timber deck and spa lit at night">
      <polygon points="603,842 691,942 648,994 560,994 487,930" fill="url(#deckGrad)"/>
    </g>

    <polygon points="0,865 251,865 355,994 0,994" fill="var(--grey-dark)"/>
    <polygon points="251,865 256,865 359,994 354,994" fill="var(--blue)"/>

    <polygon points="514,0 665,0 665,214 589,234 514,214" fill="var(--red)"/>
  </svg>

  <div class="brand">
    <div class="brand-dot"></div>
    <div class="brand-name">TORVIN ELECTRICS</div>
  </div>

  <div class="offer-badge">
    <div class="offer-big">10<sup>%</sup>OFF</div>
    <div class="offer-line l1">ALL ELECTRICAL SERVICES</div>
    <div class="offer-or">OR</div>
    <div class="offer-free">FREE LED</div>
    <div class="offer-line l2">DOWNLIGHTS ON INSTALLATION</div>
    <div class="offer-terms">*Terms conditions apply</div>
  </div>

  <div class="headline">
    <div class="h-a">SPECIALISING IN</div>
    <div class="h-b">NEW HOMES</div>
    <div class="h-c">RENOVATIONS &amp;</div>
    <div class="h-d">COMMERCIAL PROJECTS</div>
  </div>

  <div class="services-title">ALL RESIDENTIAL &amp; COMMERCIAL<br>ELECTRICAL SERVICES</div>

  <ul class="service-list list-left">
    <li>New Home installations</li>
    <li>Commercial projects</li>
    <li>Shop fit outs</li>
    <li>Renovations</li>
    <li>Smoke Detectors</li>
    <li>Air Conditioning and<br>Ceiling Fans</li>
    <li>Garden Lighting</li>
    <li>Oven and Cooktop<br>Installations</li>
  </ul>
  <div class="list-divider"></div>
  <ul class="service-list list-right">
    <li>Power Point installation</li>
    <li>LED lighting upgrades</li>
    <li>Security Lighting</li>
    <li>Switchboard upgrades</li>
    <li>Test and Tag</li>
    <li>Commercial Property</li>
    <li>General Electrical<br>Maintenance</li>
  </ul>

  <div class="contact-title">CONTACT US NOW</div>
  <ul class="contact-list">
    <li>
      <svg class="contact-icon" viewBox="0 0 16 16"><path d="M3 1l3 3-2 2c1 2 3 4 5 5l2-2 3 3-2 3C7 15 1 9 1 3z" fill="#fff"/></svg>
      0457 613 948
    </li>
    <li>
      <svg class="contact-icon" viewBox="0 0 16 16"><circle cx="8" cy="8" r="7.5" fill="#fff"/><rect x="4" y="5" width="8" height="6" fill="none" stroke="#474747" stroke-width="1.2"/><path d="M4 5l4 3 4-3" fill="none" stroke="#474747" stroke-width="1.2"/></svg>
      admin@torvinelectrics.com.au
    </li>
    <li>
      <span class="contact-dot"></span>
      TorvinElectrics
    </li>
  </ul>

  <div class="offer-ends">OFFER ENDS</div>
  <div class="offer-date">30/11/18</div>
  <div class="licence">
    <div><b>LIC NO</b> - 73518</div>
    <div class="abn"><b>ABN</b> - 48 207 915 362</div>
  </div>
</div>
</body>
</html>
```